Ridgeway Building van wrap

Company name: Ridgeway Building Works, inc.
must include:
555-392-7160
Ridgeway Building Logo
Color Match the ridgeway building blue: RGB: 1, 18, 68; CMYK: 99%, 74%, 0%, 73%; HEX: #011244
24/7 Emergency Services
White base, clean look
ideas for logo:
Icons in color for (Water, Fire, Hurricane)
Restoration
NWPRA Certified Logo
Inserted below are some ideas we like, nothing crazy, nothing too simple either.

Target Market(s)

Homeowners, business owners, developers.

Industry/Entity Type

construction

Font styles to use
Sans Serif

Colors

Designer to choose colors to be used in the design.

Requirements
Must have
• Ridgeway Building logo, phone number, and space for a QR code on the back side of the van.

```html
<!DOCTYPE html>
<html lang="en">
<head>
<meta charset="utf-8">
<title>Ridgeway Building van wrap</title>
<link href="https://fonts.googleapis.com/css2?family=Jost:wght@500;600&family=Saira+Condensed:wght@600&display=swap" rel="stylesheet">
<style>
  :root {
    --ridgeway-blue: #011244;
    --wrap-white: #f7f7f7;
    --backdrop: #d6d6d6;
    --panel-edge: #c4c4c4;
  }
  * { box-sizing: border-box; margin: 0; padding: 0; }
  html, body { width: 876px; height: 1200px; overflow: hidden; }
  body {
    background: var(--backdrop);
    font-family: "Jost", sans-serif;
    color: var(--ridgeway-blue);
    position: relative;
  }
  .wrap-panel {
    position: absolute;
    background: var(--wrap-white);
    border: 1px solid var(--panel-edge);
    border-radius: 14px;
    overflow: hidden;
  }
  .side-right { left: 24px; top: 24px; width: 828px; height: 360px; }
  .side-left  { left: 24px; top: 404px; width: 828px; height: 360px; }
  .rear-doors { left: 24px; top: 784px; width: 520px; height: 392px; }
  .hood       { left: 564px; top: 784px; width: 288px; height: 392px; }
  .place { position: absolute; }

  .brand-square {
    position: absolute;
    width: 170px; height: 170px;
    border: 14px solid var(--ridgeway-blue);
  }
  .brand-name {
    font-weight: 600;
    letter-spacing: 0.16em;
    line-height: 1.15;
    text-transform: uppercase;
    white-space: nowrap;
  }
  .brand-bar {
    background: var(--ridgeway-blue);
    color: var(--wrap-white);
    font-size: 10px;
    letter-spacing: 1.6em;
    text-transform: uppercase;
    padding: 2px 0 2px 12px;
    margin-top: 6px;
    white-space: nowrap;
    overflow: hidden;
  }
  .contact .phone {
    font-family: "Saira Condensed", sans-serif;
    font-weight: 600;
    display: flex; align-items: center; gap: 6px;
    line-height: 1;
    white-space: nowrap;
  }
  .contact .web { font-size: 11px; letter-spacing: 0.14em; margin-top: 4px; white-space: nowrap; }
  .phone-icon { flex: none; }

  .services { display: flex; align-items: flex-end; gap: 18px; }
  .service { text-align: center; font-size: 11px; font-weight: 600; text-transform: uppercase; }
  .service-mark {
    display: block; margin: 0 auto 4px;
    width: 32px; height: 32px; border-radius: 50%;
    background: var(--ridgeway-blue);
  }
  .emergency { display: flex; align-items: center; gap: 8px; }
  .calendar-mark { width: 34px; height: 38px; border: 3px solid var(--ridgeway-blue); border-radius: 4px; }
  .emergency-text { line-height: 1; font-weight: 600; text-transform: uppercase; }
  .emergency-text b { font-family: "Saira Condensed", sans-serif; font-size: 24px; display: block; }
  .emergency-text span { font-size: 10px; display: block; }

  .cert-badge {
    width: 40px; height: 52px; border-radius: 6px;
    background: var(--ridgeway-blue);
  }
  .qr-space {
    width: 70px; height: 70px; border: 2px solid var(--ridgeway-blue);
    display: flex; align-items: flex-end; justify-content: center;
    font-size: 8px; font-weight: 600; letter-spacing: 0.1em; padding-bottom: 4px;
  }
  .door-split { position: absolute; left: 260px; top: 0; bottom: 0; border-left: 1px solid var(--panel-edge); }
  .dot-mark { width: 40px; height: 40px; border-radius: 50%; background: var(--ridgeway-blue); flex: none; }
</style>
</head>
<body>

<section class="wrap-panel side-right" aria-label="Passenger side">
  <div class="place contact" style="left:34px; top:150px;">
    <div class="phone" style="font-size:32px;">
      <svg class="phone-icon" width="22" height="22" viewBox="0 0 24 24"><circle cx="12" cy="12" r="11" fill="none" stroke="#011244" stroke-width="1.6"/><path d="M8 6.5l2 2.5-1.2 1.4c.7 1.6 1.9 2.8 3.5 3.5l1.4-1.2 2.5 2-1 1.8c-4.3-.3-8-4-8.3-8.3z" fill="#011244"/></svg>
      (555) 392-7160
    </div>
    <div class="web">www.RidgewayBuilding.net</div>
  </div>
  <div class="brand-square" style="left:290px; top:80px;"></div>
  <div class="place" style="left:480px; top:60px;">
    <div class="brand-name" style="font-size:28px;">Ridgeway<br>Building</div>
    <div class="brand-bar" style="width:320px;">Restoration</div>
  </div>
  <div class="place services" style="left:480px; top:214px; gap:14px;">
    <div class="emergency"><div class="calendar-mark" role="img" aria-label="Calendar with clock icon"></div><div class="emergency-text"><b>24/7</b><span>Emergency<br>Services</span></div></div>
    <div class="service"><i class="service-mark" role="img" aria-label="Water damage icon"></i>Water</div>
    <div class="service"><i class="service-mark" role="img" aria-label="Fire damage icon"></i>Fire</div>
    <div class="service"><i class="service-mark" role="img" aria-label="Hurricane damage icon"></i>Hurricane</div>
  </div>
  <div class="place cert-badge" style="left:770px; top:290px;" role="img" aria-label="Certification badge"></div>
</section>

<section class="wrap-panel side-left" aria-label="Driver side">
  <div class="place" style="left:40px; top:60px;">
    <div class="brand-name" style="font-size:28px;">Ridgeway<br>Building</div>
    <div class="brand-bar" style="width:330px;">Restoration</div>
  </div>
  <div class="place services" style="left:40px; top:200px; gap:14px;">
    <div class="emergency"><div class="calendar-mark" role="img" aria-label="Calendar with clock icon"></div><div class="emergency-text"><b>24/7</b><span>Emergency<br>Services</span></div></div>
    <div class="service"><i class="service-mark" role="img" aria-label="Water damage icon"></i>Water</div>
    <div class="service"><i class="service-mark" role="img" aria-label="Fire damage icon"></i>Fire</div>
    <div class="service"><i class="service-mark" role="img" aria-label="Hurricane damage icon"></i>Hurricane</div>
  </div>
  <div class="place cert-badge" style="left:40px; top:280px;" role="img" aria-label="Certification badge"></div>
  <div class="brand-square" style="left:392px; top:90px;"></div>
  <div class="place contact" style="left:585px; top:180px;">
    <div class="phone" style="font-size:32px;">
      <svg class="phone-icon" width="22" height="22" viewBox="0 0 24 24"><circle cx="12" cy="12" r="11" fill="none" stroke="#011244" stroke-width="1.6"/><path d="M8 6.5l2 2.5-1.2 1.4c.7 1.6 1.9 2.8 3.5 3.5l1.4-1.2 2.5 2-1 1.8c-4.3-.3-8-4-8.3-8.3z" fill="#011244"/></svg>
      (555) 392-7160
    </div>
    <div class="web">www.RidgewayBuilding.net</div>
  </div>
</section>

<section class="wrap-panel rear-doors" aria-label="Rear doors">
  <div class="door-split"></div>
  <div class="place" style="left:36px; top:40px; display:flex; gap:12px; align-items:center;">
    <div class="dot-mark"></div>
    <div class="brand-name" style="font-size:20px;">Ridgeway<br>Building</div>
  </div>
  <div class="place brand-bar" style="left:36px; top:110px; width:420px;">Restoration</div>
  <div class="place contact" style="left:36px; top:150px;">
    <div class="phone" style="font-size:28px;">
      <svg class="phone-icon" width="20" height="20" viewBox="0 0 24 24"><circle cx="12" cy="12" r="11" fill="none" stroke="#011244" stroke-width="1.6"/><path d="M8 6.5l2 2.5-1.2 1.4c.7 1.6 1.9 2.8 3.5 3.5l1.4-1.2 2.5 2-1 1.8c-4.3-.3-8-4-8.3-8.3z" fill="#011244"/></svg>
      (555) 392-7160
    </div>
    <div class="web">www.RidgewayBuilding.net</div>
  </div>
  <div class="place emergency" style="left:36px; top:220px;"><div class="calendar-mark" role="img" aria-label="Calendar with clock icon"></div><div class="emergency-text"><b>24/7</b><span>Emergency<br>Services</span></div></div>
  <div class="place services" style="left:36px; top:296px; gap:14px;">
    <div class="service"><i class="service-mark" role="img" aria-label="Water damage icon"></i>Water</div>
    <div class="service"><i class="service-mark" role="img" aria-label="Fire damage icon"></i>Fire</div>
    <div class="service"><i class="service-mark" role="img" aria-label="Hurricane damage icon"></i>Hurricane</div>
  </div>
  <div class="place qr-space" style="left:300px; top:290px;">SCAN ME</div>
  <div class="place cert-badge" style="left:400px; top:298px;" role="img" aria-label="Certification badge"></div>
</section>

<section class="wrap-panel hood" aria-label="Hood">
  <div class="place" style="left:0; right:0; top:150px; display:flex; flex-direction:column; align-items:center; gap:12px;">
    <div class="dot-mark" style="width:56px; height:56px;"></div>
    <div class="brand-name" style="font-size:18px; text-align:center;">Ridgeway Building</div>
  </div>
</section>

</body>
</html>
```